Please redesign the attached signage to a larger dimensions 6000mm wide x 3000mm high.

this is for large format digital printing.

Target Market(s)

Clients buying cars from car dealerships

Industry/Entity Type

Digital

Font styles to use
Sans Serif

Colors

Designer to choose colors to be used in the design.

```html
<!DOCTYPE html>
<html lang="en">
<head>
<meta charset="utf-8">
<title>Buy Here Pay Here – Signage</title>
<link rel="stylesheet" href="https://fonts.googleapis.com/css2?family=Arimo:ital,wght@1,700&display=swap">
<style>
  :root {
    --sky-top: #1f7fc4;
    --sky-mid: #2a3f93;
    --sky-base: #27388a;
    --lot-grey: #8e9094;
    --lineup-light: #a3a5a9;
    --lineup-dark: #7d7f83;
    --asphalt: #2b2b2d;
    --signal-red: #e8112d;
    --deep-red: #8f0a1a;
    --white: #ffffff;
  }
  * { margin: 0; padding: 0; box-sizing: border-box; }
  html, body { width: 1200px; height: 626px; overflow: hidden; background: var(--asphalt); }
  .sign {
    position: relative;
    width: 1200px;
    height: 626px;
    overflow: hidden;
    font-family: "Arimo", Arial, Helvetica, sans-serif;
    font-weight: 700;
    font-style: italic;
  }
  .sky-band {
    position: absolute; left: 0; top: 0; width: 1200px; height: 173px;
    background: linear-gradient(to bottom, var(--sky-top) 0%, var(--sky-mid) 30%, var(--sky-base) 100%);
  }
  .lot-band {
    position: absolute; left: 0; top: 173px; width: 1200px; height: 304px;
    background: var(--lot-grey);
  }
  .ground-band {
    position: absolute; left: 0; top: 477px; width: 1200px; height: 149px;
    background: var(--asphalt);
  }
  .headline {
    position: absolute; left: 0; top: 30px; width: 1200px;
    text-align: center;
    font-size: 102px; line-height: 1; letter-spacing: -1px;
    font-weight: 700;
    color: var(--signal-red);
    text-shadow:
      2px 0 0 var(--white), -2px 0 0 var(--white), 0 2px 0 var(--white), 0 -2px 0 var(--white),
      2px 2px 0 var(--white), -2px -2px 0 var(--white), 2px -2px 0 var(--white), -2px 2px 0 var(--white),
      4px 4px 0 var(--deep-red);
  }
  .vehicle-lineup {
    position: absolute; left: 12px; top: 150px; width: 1188px; height: 224px;
    background: linear-gradient(to bottom, var(--lineup-light) 0%, var(--lineup-dark) 100%);
  }
  .offer-box {
    position: absolute; left: 84px; top: 386px; width: 1040px; height: 128px;
    background: var(--signal-red);
    border: 6px solid var(--white);
    display: flex; align-items: center; justify-content: center;
  }
  .offer-text {
    color: var(--white);
    font-size: 72px; line-height: 1;
    letter-spacing: -0.5px;
  }
  .accepted-list {
    position: absolute; left: 0; top: 537px; width: 1200px;
    display: flex; justify-content: center; gap: 10px;
    list-style: none;
  }
  .accepted-item {
    display: flex; align-items: center; gap: 3px;
    color: var(--white);
    font-size: 36px; line-height: 1;
    letter-spacing: -0.3px;
  }
  .tick-icon { width: 33px; height: 33px; flex: none; }
</style>
</head>
<body>
  <div class="sign">
    <div class="sky-band"></div>
    <div class="lot-band"></div>
    <div class="ground-band"></div>

    <div class="vehicle-lineup" role="img" aria-label="Illustration of a row of used cars for sale"></div>

    <h1 class="headline">BUY HERE PAY HERE</h1>

    <div class="offer-box">
      <p class="offer-text">Bad Credit? No Problem!</p>
    </div>

    <ul class="accepted-list">
      <li class="accepted-item">
        <svg class="tick-icon" viewBox="0 0 34 34" aria-hidden="true"><circle cx="17" cy="17" r="15" fill="#e8112d" stroke="#fff" stroke-width="2.5"/><path d="M10 17.5l5 5 9-10" fill="none" stroke="#fff" stroke-width="3.5" stroke-linecap="round" stroke-linejoin="round"/></svg>
        Bankruptcy
      </li>
      <li class="accepted-item">
        <svg class="tick-icon" viewBox="0 0 34 34" aria-hidden="true"><circle cx="17" cy="17" r="15" fill="#e8112d" stroke="#fff" stroke-width="2.5"/><path d="M10 17.5l5 5 9-10" fill="none" stroke="#fff" stroke-width="3.5" stroke-linecap="round" stroke-linejoin="round"/></svg>
        Foreclosures
      </li>
      <li class="accepted-item">
        <svg class="tick-icon" viewBox="0 0 34 34" aria-hidden="true"><circle cx="17" cy="17" r="15" fill="#e8112d" stroke="#fff" stroke-width="2.5"/><path d="M10 17.5l5 5 9-10" fill="none" stroke="#fff" stroke-width="3.5" stroke-linecap="round" stroke-linejoin="round"/></svg>
        Repossession
      </li>
      <li class="accepted-item">
        <svg class="tick-icon" viewBox="0 0 34 34" aria-hidden="true"><circle cx="17" cy="17" r="15" fill="#e8112d" stroke="#fff" stroke-width="2.5"/><path d="M10 17.5l5 5 9-10" fill="none" stroke="#fff" stroke-width="3.5" stroke-linecap="round" stroke-linejoin="round"/></svg>
        Charge Offs
      </li>
    </ul>
  </div>
</body>
</html>
```